Business Card Design Project

Bold, modern, clean business card design needed. Prefer double sided with art logo on the back. Front of card with company name logo, no art.

Target Market(s)

Our consulting company supports local, state and federal law enforcement officers. Therefore the design should be clean and direct with no flash or arrogance to it.

Industry/Entity Type

Business

```html
<!DOCTYPE html>
<html lang="en">
<head>
<meta charset="utf-8">
<title>Halvard Advisory — Business Cards</title>
<link rel="stylesheet" href="https://fonts.googleapis.com/css2?family=Michroma&family=Oswald:wght@700&family=Open+Sans:wght@400;600&display=swap">
<style>
  :root {
    --canvas: #e9e9e7;
    --card: #ffffff;
    --green: #8cc63f;
    --green-dark: #74ab2c;
    --ink: #1a1a1a;
    --swoosh: #9a9a9a;
    --muted: #555555;
  }
  * { box-sizing: border-box; margin: 0; padding: 0; }
  html, body { width: 1200px; height: 873px; overflow: hidden; }
  body {
    background: var(--canvas);
    display: flex;
    align-items: center;
    justify-content: center;
    gap: 60px;
    font-family: "Open Sans", sans-serif;
  }
  .card {
    position: relative;
    width: 520px;
    height: 297px;
    background: var(--card);
    box-shadow: 0 6px 18px rgba(0,0,0,0.12);
    overflow: hidden;
  }
  .card-front .band { position: absolute; inset: 0; }
  .contact-list {
    position: absolute;
    top: 14px;
    left: 22px;
    list-style: none;
    color: #ffffff;
    font-size: 10px;
    line-height: 1;
  }
  .contact-list li { display: flex; align-items: center; gap: 8px; margin-bottom: 7px; }
  .contact-list svg { width: 12px; height: 12px; flex: none; }
  .brand {
    position: absolute;
    display: flex;
    align-items: center;
    gap: 10px;
  }
  .brand-mark { border-radius: 50%; background: var(--green); flex: none; }
  .brand-name {
    font-family: "Michroma", sans-serif;
    color: var(--ink);
    letter-spacing: 0.04em;
    line-height: 1.15;
  }
  .card-front .brand { left: 30px; top: 122px; }
  .card-front .brand-mark { width: 22px; height: 22px; }
  .card-front .brand-name { font-size: 17px; }
  .holder {
    position: absolute;
    right: 34px;
    bottom: 36px;
    text-align: left;
  }
  .holder-name {
    font-family: "Oswald", sans-serif;
    font-weight: 700;
    font-size: 30px;
    color: var(--ink);
    text-transform: uppercase;
    line-height: 1;
    display: flex;
    gap: 4px;
  }
  .holder-name .accent { background: var(--green); color: #fff; padding: 0 4px; }
  .holder-role {
    display: flex;
    align-items: center;
    gap: 8px;
    margin-top: 6px;
    font-size: 12px;
    font-weight: 600;
    letter-spacing: 0.28em;
    color: var(--ink);
  }
  .holder-role .bar { width: 26px; height: 12px; border: 3px solid var(--green); }
  .card-back { display: flex; align-items: center; justify-content: center; }
  .card-back .brand { position: static; flex-direction: column; gap: 14px; }
  .card-back .brand-mark { width: 46px; height: 46px; }
  .card-back .brand-name { font-size: 24px; text-align: center; }
</style>
</head>
<body>
  <section class="card card-front" aria-label="Card front">
    <svg class="band" viewBox="0 0 520 297" preserveAspectRatio="none" aria-hidden="true">
      <path d="M0 0 H520 V6 C400 30 300 40 200 70 C120 95 50 118 0 128 Z" fill="var(--swoosh)"/>
      <path d="M0 0 H520 V0 C400 22 300 32 200 62 C120 86 50 108 0 118 Z" fill="var(--green)"/>
    </svg>
    <ul class="contact-list">
      <li>
        <svg viewBox="0 0 12 12"><rect x="0.5" y="2" width="11" height="8" fill="none" stroke="#fff"/><path d="M0.5 2 L6 7 L11.5 2" fill="none" stroke="#fff"/></svg>
        email@example.com
      </li>
      <li>
        <svg viewBox="0 0 12 12"><rect x="3" y="0.5" width="6" height="11" rx="1" fill="none" stroke="#fff"/><circle cx="6" cy="9.5" r="0.7" fill="#fff"/></svg>
        111-344-544
      </li>
      <li>
        <svg viewBox="0 0 12 12"><path d="M6 11.5 C3 7.5 2 6 2 4.5 A4 4 0 0 1 10 4.5 C10 6 9 7.5 6 11.5 Z" fill="none" stroke="#fff"/><circle cx="6" cy="4.5" r="1.3" fill="#fff"/></svg>
        Your Location Here
      </li>
    </ul>
    <div class="brand">
      <span class="brand-mark" aria-hidden="true"></span>
      <span class="brand-name">HALVARD<br>ADVISORY</span>
    </div>
    <div class="holder">
      <p class="holder-name"><span>Your</span><span class="accent">Name</span></p>
      <p class="holder-role">POSITION <span class="bar" aria-hidden="true"></span></p>
    </div>
  </section>

  <section class="card card-back" aria-label="Card back">
    <div class="brand">
      <span class="brand-mark" aria-hidden="true"></span>
      <span class="brand-name">HALVARD<br>ADVISORY</span>
    </div>
  </section>
</body>
</html>
```